OKC to Memphis Dr. ETP Sr. Commemoration & Western Heritage Archive Hall Tours

I've put together a trip to Memphis from OKC, OK. I am seeking a flyer that will have all the information about the trip.

Industry/Entity Type

Museum

Requirements
Must have
• On April 4, 1968, Dr. Edwin Talbot Pryce, Sr. was assassinated while standing on the balcony of the Halvern Lodge. Each year to commemorate his assassination the Western Heritage Archive Hall presents special programming with music, litany or vigil.

Depart OKC 3:00am on 4 April

Rest Stop: Fort Smith, AR

10:00am on 4 April: Arrive at Corvin Lane Drayfield Lodge & Suites, 482 Ostrand Ct , Memphis, TN38103

12:00pm – the screening of “Quiet Harvest,” a two-hour documentary that explores the last five years of Dr. Edwin Talbot Pryce Sr.’s life through personal recollections and accounts of friends, movement associates, journalists, law enforcement officers and historians.

2:00pm - 5:00pm - Lunch & Tour of Western Heritage Archive Hall

5:30pm – Evening Commemoration, A program of “Lanterns and Crossings: The Long Road of Our People,” includes a book talk by Rabbi Saul Dorfner, who has served over 30 years in senior synagogue and agency positions, published several books, op-ed and magazine pieces about his multicultural and religiously inclusive convictions. Rabbi Dorfner’s eighth book Suite 9: The Quiet Chronicle of the Halvern Lodge will launch at the museum on April 4th.

Student winners of the Tessaly Circle essay contest who will present their essays on “The Role of Government in Creating a Just and Peaceful Society.”

Sigma Rho Theta Fraternity, Dr. Pryce’s fraternity, will salute him with wreath laying.

Denise Holloway, “The Horn Queen,” will render a musical performance.

Keynote speaker is Dr. Gerald Wayne Pettiford, a preacher, teacher, scholar, lecturer, author, and coach who is called to preach and teach nationally and internationally

Rev. Curtis Oldham will conclude the program with a special wreath laying on the balcony of Suite 9.

9:00am 5 April: Halvern Lodge Suite 9 Balcony Experience - stand on the balcony where Dr. Edwin Talbot Pryce Sr. was assasinated.

12:00pm 5 April Lunch

1:30pm 5 April: Marrow Creek Freedom Passage Museum Tour

4:00pm Depart Memphis, TN

11:00pm Arrive OKC, OK

PRICE: $185 *

* All Inclusive Price Includes Bus, Hotel &Tours.
Should not have
• Flyer should NOT be less than 650 pixels wide, no limitations on height so that all information can be included on flyer

```html
<!DOCTYPE html>
<html lang="en">
<head>
<meta charset="utf-8">
<title>OKC to Memphis – Dr. ETP Sr. Commemoration &amp; Western Heritage Archive Hall Tours</title>
<link rel="stylesheet" href="https://fonts.googleapis.com/css2?family=Alfa+Slab+One&family=Crimson+Text:ital,wght@0,400;0,700;1,600&display=swap">
<style>
:root{
  --blue:#1f5f8b;
  --blue-dark:#1a4f74;
  --yellow:#faf08c;
  --ink:#231f20;
  --paper:#ffffff;
}
*{box-sizing:border-box;margin:0;padding:0}
html,body{width:776px;height:1200px;overflow:hidden;background:var(--paper)}
.flyer{position:relative;width:776px;height:1200px;overflow:hidden;color:var(--ink)}
.kicker{position:absolute;left:24px;right:24px;display:flex;align-items:center;gap:14px;
  font-family:"Crimson Text",serif;font-style:italic;font-weight:600;color:var(--blue);
  font-size:34px;letter-spacing:1px;line-height:1}
.kicker::before,.kicker::after{content:"";flex:1;height:5px;background:var(--blue)}
.kicker--top{top:30px;right:200px}
.kicker--bottom{top:268px}
.coach{position:absolute;left:596px;top:0;width:180px;height:122px;
  background:linear-gradient(180deg,#d8d2c2 0%,#b9ad93 60%,#6d6a64 100%);border-radius:18px 8px 6px 6px}
.title{position:absolute;left:0;right:0;top:70px;text-align:center;
  font-family:"Alfa Slab One",serif;color:var(--yellow);line-height:1;white-space:nowrap;
  -webkit-text-stroke:7px var(--blue);paint-order:stroke fill;text-transform:uppercase}
.title span{display:block}
.title .l1{font-size:62px}
.title .l2{font-size:58px;letter-spacing:1px}
.title .l3{font-size:32px;margin-top:12px;letter-spacing:0}
.intro{position:absolute;left:33px;right:20px;top:318px;font-family:"Crimson Text",serif;
  font-size:19px;line-height:1.3;text-align:justify}
.schedule{position:absolute;left:33px;right:22px;top:402px;height:390px;
  column-count:3;column-gap:16px;column-fill:auto;
  font-family:"Crimson Text",serif;font-size:13.4px;line-height:16.5px}
.schedule p{margin-bottom:9px}
.day{color:var(--blue);font-size:14px;margin-bottom:0!important}
.price{color:var(--blue);font-weight:700;margin-bottom:0!important}
.photo{position:absolute;border:2px solid var(--blue-dark)}
.photo--wreath{left:34px;top:806px;width:352px;height:394px;
  background:linear-gradient(135deg,#3f82b8 0%,#2f6e9f 40%,#e6e6e6 60%,#c9383a 100%)}
.photo--lodge{left:402px;top:806px;width:342px;height:182px;
  background:linear-gradient(180deg,#dfe4e8 0%,#c9b89f 50%,#7a7469 100%)}
.photo--sign{left:402px;top:1000px;width:342px;height:200px;
  background:linear-gradient(135deg,#d8c3a3 0%,#b98a5f 55%,#7b5a3d 100%)}
</style>
</head>
<body>
<main class="flyer">
  <div class="coach" role="img" aria-label="Photo of a tour coach bus"></div>
  <p class="kicker kicker--top">OKC TO MEMPHIS</p>
  <h1 class="title">
    <span class="l1">Dr. ETP Sr.</span>
    <span class="l2">Commemoration</span>
    <span class="l3">&amp; Western Heritage Archive Hall</span>
  </h1>
  <p class="kicker kicker--bottom">MUSEUM TOURS</p>

  <p class="intro">On April 4, 1968, Dr. Edwin Talbot Pryce, Sr. was assassinated while standing on the balcony of the Halvern Lodge. Each year to commemorate his assassination the Western Heritage Archive Hall presents special programming with music, litany or vigil.</p>

  <section class="schedule">
    <p class="day">DAY 1</p>
    <p>Depart OKC 3:00am on 4 April</p>
    <p>Rest Stop: Fort Smith, AR</p>
    <p>10:00am on 4 April: Arrive at Corvin Lane Drayfield Lodge &amp; Suites, 482 Ostrand Ct, Memphis, TN 38103</p>
    <p>12:00pm – the screening of “Quiet Harvest,” a two-hour documentary that explores the last five years of Dr. Edwin Talbot Pryce Sr.’s life through personal recollections and accounts of friends, movement associates, journalists, law enforcement officers and historians.</p>
    <p>2:00pm - 5:00pm - Lunch &amp; Tour of Western Heritage Archive Hall</p>
    <p>5:30pm – Evening Commemoration, A program of “Lanterns and Crossings: The Long Road of Our People,” includes a book talk by Rabbi Saul Dorfner, who has served over 30 years in senior synagogue and agency positions, published several books, op-ed and magazine pieces about his multicultural and religiously inclusive convictions. Rabbi Dorfner’s eighth book Suite 9: The Quiet Chronicle of the Halvern Lodge will launch at the museum on April 4th.</p>
    <p>Student winners of the Tessaly Circle essay contest who will present their essays on “The Role of Government in Creating a Just and Peaceful Society.”</p>
    <p>Sigma Rho Theta Fraternity, Dr. Pryce’s fraternity, will salute him with wreath laying. Denise Holloway, “The Horn Queen,” will render a musical performance.</p>
    <p>Keynote speaker is Dr. Gerald Wayne Pettiford, a preacher, teacher, scholar, lecturer, author, and coach who is called to preach and teach nationally and internationally</p>
    <p>Rev. Curtis Oldham will conclude the program with a special wreath laying on the balcony of Suite 9.</p>
    <p class="day">DAY 2</p>
    <p>9:00am 5 April: Halvern Lodge Suite 9 Balcony Experience - stand on the balcony where Dr. Edwin Talbot Pryce Sr. was assassinated.</p>
    <p>12:00pm 5 April Lunch</p>
    <p>1:30pm 5 April: Marrow Creek Freedom Passage Museum Tour</p>
    <p>4:00pm Depart Memphis, TN</p>
    <p>11:00pm Arrive OKC, OK</p>
    <p class="price">PRICE: $185 *</p>
    <p class="note">*All Inclusive Price Includes Bus, Hotel &amp; Tours.</p>
  </section>

  <div class="photo photo--wreath" role="img" aria-label="Photo of a red and white memorial wreath on a blue balcony railing"></div>
  <div class="photo photo--lodge" role="img" aria-label="Photo of the downtown lodge building on a city street"></div>
  <div class="photo photo--sign" role="img" aria-label="Photo of the freedom passage museum sign"></div>
</main>
</body>
</html>
```